Business Card Design

This is a new business We need a business card that shows that we can do whatever people require for maintaining a building we all so like to Achieve a green star feel about the card and Eco Friendly Properly maintenance Building & Construction cleaning,Carpet Cleaning ,Pressure Cleaning Move in Move Out CleaningRubbish RemovalLawn Mowing & Edging>Who we serveCommercial DevelopersResidential BuildersProperty ManagersBuilding Owners Home Owners Real Estate Agents

Target Market(s)

Building & construction

Industry/Entity Type

Property Maintenance

Contact Information for Business Card

Brightmoor Property Maintenance Colin Ratcliffe Unit 3 / 8 Ferndale Road Kelsworth 3915Victoria Southland Ph 0427365918

Font styles to use
Sans Serif
Script

Colors
9ccb3b
aaaaaa

Requirements
Must have
• Have eco friendly feel

```html
<!DOCTYPE html>
<html lang="en">
<head>
<meta charset="utf-8">
<title>Brightmoor — Business Card</title>
<link href="https://fonts.googleapis.com/css2?family=Quicksand:wght@300&family=Arimo:wght@400&display=swap" rel="stylesheet">
<style>
  :root {
    --brand-green: #9ccb3b;
    --green-light: #b9de6b;
    --green-deep: #86bb2c;
    --brand-grey: #aaaaaa;
    --text-grey: #8a8a8a;
    --card-white: #ffffff;
    --backdrop: #1c1c1c;
  }
  * { margin: 0; padding: 0; box-sizing: border-box; }
  html, body { width: 1200px; height: 871px; overflow: hidden; }
  body { background: var(--backdrop); position: relative; }

  .card {
    position: absolute;
    width: 600px;
    height: 343px;
    overflow: hidden;
    border-radius: 3px;
  }

  /* Front: green */
  .card--front {
    left: 70px; top: 70px;
    background: linear-gradient(135deg, var(--green-light) 0%, var(--brand-green) 45%, var(--green-deep) 100%);
  }
  .front-wordmark {
    position: absolute;
    left: 0; right: 0; top: 146px;
    display: flex;
    justify-content: center;
    align-items: center;
    gap: 14px;
    font-family: "Arimo", sans-serif;
    font-weight: 400;
    font-size: 40px;
    line-height: 1;
    color: var(--card-white);
  }
  .front-wordmark .mark-dot {
    width: 22px; height: 22px;
    border-radius: 50%;
    background: var(--card-white);
  }

  /* Back: white */
  .card--back {
    left: 530px; top: 458px;
    background: var(--card-white);
  }
  .back-wordmark {
    position: absolute;
    left: 60px; top: 84px;
    display: flex;
    align-items: center;
    gap: 10px;
    font-family: "Arimo", sans-serif;
    font-weight: 400;
    font-size: 26px;
    line-height: 1;
    color: var(--brand-green);
  }
  .back-wordmark .mark-dot {
    width: 15px; height: 15px;
    border-radius: 50%;
    background: var(--brand-green);
  }
  .divider {
    position: absolute;
    left: 0; top: 148px;
    width: 340px; height: 4px;
    background: var(--brand-green);
  }
  .person-name {
    position: absolute;
    left: 350px; top: 132px;
    font-family: "Quicksand", sans-serif;
    font-weight: 300;
    font-size: 31px;
    letter-spacing: 1px;
    color: var(--text-grey);
    white-space: nowrap;
  }
  .contact-list {
    position: absolute;
    left: 22px; top: 172px;
    list-style: none;
    font-family: "Arimo", sans-serif;
    font-size: 14px;
    color: var(--text-grey);
  }
  .contact-item {
    display: flex;
    align-items: flex-start;
    gap: 10px;
    margin-bottom: 9px;
    line-height: 19px;
  }
  .contact-icon { width: 19px; height: 19px; flex: none; }
  .contact-icon circle { fill: none; stroke: var(--brand-green); stroke-width: 1.6; }
  .contact-icon .glyph { fill: var(--brand-green); }
  .bottom-band {
    position: absolute;
    left: 0; right: 0; bottom: 0;
    height: 26px;
    background: var(--brand-green);
  }
</style>
</head>
<body>

<section class="card card--front" aria-label="Card front">
  <div class="front-wordmark"><span class="mark-dot"></span><span>Brightmoor</span></div>
</section>

<section class="card card--back" aria-label="Card back">
  <div class="back-wordmark"><span class="mark-dot"></span><span>Brightmoor</span></div>
  <div class="divider"></div>
  <div class="person-name">Colin Ratcliffe</div>

  <ul class="contact-list">
    <li class="contact-item">
      <svg class="contact-icon" viewBox="0 0 20 20" aria-hidden="true">
        <circle cx="10" cy="10" r="8.5"/>
        <path class="glyph" d="M7 5.5c.6-.4 1.2-.3 1.5.3l.8 1.6c.2.5 0 .9-.4 1.2l-.5.3c.4 1 1.2 1.9 2.2 2.4l.4-.5c.3-.4.8-.5 1.2-.3l1.5.9c.5.3.6.9.2 1.4-.7.9-1.6 1.2-2.6.8-2.4-1-4.3-3-5-5.4-.3-1.1 0-2 .7-2.7z"/>
      </svg>
      <span>042.736.5918</span>
    </li>
    <li class="contact-item">
      <svg class="contact-icon" viewBox="0 0 20 20" aria-hidden="true">
        <circle cx="10" cy="10" r="8.5"/>
        <text class="glyph" x="10" y="14" text-anchor="middle" font-family="Arimo, sans-serif" font-size="11" font-weight="700">@</text>
      </svg>
      <span>colin.ratcliffe@brightmoorpm.com</span>
    </li>
    <li class="contact-item">
      <svg class="contact-icon" viewBox="0 0 20 20" aria-hidden="true">
        <circle cx="10" cy="10" r="8.5"/>
        <path class="glyph" d="M10 4.8l5 4.4h-1.5v5H11v-3H9v3H6.5v-5H5z"/>
      </svg>
      <span>Unit 3 / 8 Ferndale Road Kelsworth,<br>3842 Eastvale, Southland</span>
    </li>
  </ul>

  <div class="bottom-band"></div>
</section>

</body>
</html>
```